IT Company based on Biology Business Needs a Business Card Design

We need a business card design for a new company called 'Lumen CELL'. We develop the machine learning solutions especially focused on deep learning algorithms for biology industry. Our initial product is a vision detection on biological images to help doctors diagnose the symptoms. We would like to see designs that use the color green.

Industry/Entity Type

Business

```html
<!DOCTYPE html>
<html lang="en">
<head>
<meta charset="utf-8">
<title>Lumen CELL — Business Card</title>
<link href="https://fonts.googleapis.com/css2?family=Open+Sans:wght@400;600;700&display=swap" rel="stylesheet">
<style>
  :root {
    --stage: #2b2b2b;
    --paper: #f7f8f7;
    --paper-shade: #ecefec;
    --green: #18a24a;
    --green-dark: #0f8a3a;
    --green-light: #7cc242;
    --pattern-a: #e6efe3;
    --pattern-b: #dbe7dd;
    --ink: #1f3b4a;
    --ink-soft: #4a4f52;
    --white: #ffffff;
  }
  * { box-sizing: border-box; margin: 0; padding: 0; }
  html, body { width: 1200px; height: 834px; overflow: hidden; }
  body {
    background: var(--stage);
    font-family: "Open Sans", Arial, sans-serif;
    position: relative;
  }
  .card {
    position: absolute;
    left: 290px;
    width: 620px;
    height: 354px;
    background: linear-gradient(135deg, var(--white), var(--paper) 60%, var(--paper-shade));
    overflow: hidden;
    box-shadow: 0 6px 18px rgba(0,0,0,.45);
  }
  .card--back { top: 46px; }
  .card--front { top: 432px; }

  /* Back side */
  .back-pattern {
    position: absolute; inset: 0;
    background: linear-gradient(160deg, var(--pattern-a), var(--paper) 50%, var(--pattern-b));
  }
  .back-band {
    position: absolute; left: 0; right: 0; top: 140px; height: 72px;
    background: var(--green);
    display: flex; align-items: center; justify-content: center;
  }
  .back-band__url {
    color: var(--white); font-size: 15px; font-weight: 400; letter-spacing: .3px;
  }

  /* Front side */
  .front-ornament {
    position: absolute; left: 0; top: 70px; width: 150px; height: 260px;
    background: linear-gradient(90deg, rgba(24,162,74,.35), rgba(124,194,66,.12) 70%, rgba(124,194,66,0));
  }
  .front-name {
    position: absolute; left: 150px; top: 58px;
    font-size: 17px; font-weight: 700; color: var(--ink);
  }
  .front-name__role { font-weight: 400; color: var(--green-light); }
  .contact {
    position: absolute; display: flex; align-items: center; gap: 12px;
    font-size: 12px; color: var(--ink-soft);
  }
  .contact__icon {
    width: 28px; height: 28px; border-radius: 50%;
    background: var(--green); display: flex; align-items: center; justify-content: center;
    flex: none;
  }
  .contact__icon--light { background: var(--green-light); }
  .contact__icon svg { width: 15px; height: 15px; }
  .contact--address { left: 150px; top: 120px; }
  .contact--mobile  { left: 168px; top: 162px; }
  .contact--phone   { left: 196px; top: 204px; }
  .contact--email   { left: 224px; top: 246px; }
  .contact--web     { left: 232px; top: 288px; }

  .brand {
    position: absolute; left: 392px; top: 100px;
    display: flex; align-items: center; gap: 10px;
  }
  .brand__dot { width: 22px; height: 22px; border-radius: 50%; background: var(--green); }
  .brand__name { font-size: 30px; font-weight: 600; color: var(--green); letter-spacing: -.5px; }
</style>
</head>
<body>

<section class="card card--back" aria-label="Card back">
  <div class="back-pattern" role="img" aria-label="Faint green molecular pattern background"></div>
  <div class="back-band"><span class="back-band__url">www.lumencell.com</span></div>
</section>

<section class="card card--front" aria-label="Card front">
  <div class="front-ornament" role="img" aria-label="Green molecule-stick decoration along the left edge"></div>

  <p class="front-name">Mara Ellison - <span class="front-name__role">President</span></p>

  <div class="contact contact--address">
    <span class="contact__icon contact__icon--light">
      <svg viewBox="0 0 16 16"><path d="M8 1.5a4.5 4.5 0 0 0-4.5 4.5c0 3.4 4.5 8.5 4.5 8.5s4.5-5.1 4.5-8.5A4.5 4.5 0 0 0 8 1.5z" fill="#fff"/><circle cx="8" cy="6" r="1.7" fill="#7cc242"/></svg>
    </span>
    <span>12 Fenwick Row, York, UK, YO1 4QP</span>
  </div>

  <div class="contact contact--mobile">
    <span class="contact__icon contact__icon--light">
      <svg viewBox="0 0 16 16"><rect x="4.5" y="1.5" width="7" height="13" rx="1.2" fill="none" stroke="#fff" stroke-width="1.3"/><circle cx="8" cy="12.3" r=".8" fill="#fff"/></svg>
    </span>
    <span>+44 (0) 7700 900 312</span>
  </div>

  <div class="contact contact--phone">
    <span class="contact__icon">
      <svg viewBox="0 0 16 16"><path d="M2 6c0-2 3-3.5 6-3.5S14 4 14 6l-2.5.8-.8-1.6H5.3l-.8 1.6z" fill="#fff"/><rect x="4" y="8" width="8" height="5" rx="1" fill="none" stroke="#fff" stroke-width="1.3"/></svg>
    </span>
    <span>+44 (0) 7700 900 487</span>
  </div>

  <div class="contact contact--email">
    <span class="contact__icon">
      <svg viewBox="0 0 16 16"><rect x="2" y="4" width="12" height="8.5" rx="1" fill="none" stroke="#fff" stroke-width="1.3"/><path d="M2.5 4.5 8 9l5.5-4.5" fill="none" stroke="#fff" stroke-width="1.3"/></svg>
    </span>
    <span>mara@lumencell.life</span>
  </div>

  <div class="contact contact--web">
    <span class="contact__icon">
      <svg viewBox="0 0 16 16"><circle cx="8" cy="8" r="5.8" fill="none" stroke="#fff" stroke-width="1.2"/><ellipse cx="8" cy="8" rx="2.5" ry="5.8" fill="none" stroke="#fff" stroke-width="1.1"/><path d="M2.3 8h11.4" stroke="#fff" stroke-width="1.1"/></svg>
    </span>
    <span>www.lumencell.life</span>
  </div>

  <div class="brand">
    <span class="brand__dot"></span>
    <span class="brand__name">LUMEN CELL</span>
  </div>
</section>

</body>
</html>
```